New Coffee Packaging

Update/refresh/modernize range of 1 kg Coffee packaging

Industry/Entity Type

Hospitalty

Requirements
Must have
• Clean. crisp, eye catching
Nice to have
• Vendra means 'Height' specialty coffee is grown at high altitudes, peaks. mountains

```html
<!DOCTYPE html>
<html lang="en">
<head>
<meta charset="utf-8">
<title>Vendra Coffee Co. – 1kg Packaging Range</title>
<link href="https://fonts.googleapis.com/css2?family=Josefin+Sans:wght@400;600;700&display=swap" rel="stylesheet">
<style>
  :root{
    --ink:#2b2b2b;
    --rule:#9a9a9a;
    --paper:#ffffff;
    --backdrop:#efede9;
    --gold:#b8861b;
    --green:#6db33f;
    --navy:#283b7c;
    --red:#d3283a;
    --pattern-dark:#2b2b2b;
  }
  *{box-sizing:border-box;margin:0;padding:0}
  html,body{width:1200px;height:3000px;overflow:hidden}
  body{background:var(--backdrop);font-family:"Josefin Sans",sans-serif;color:var(--ink);position:relative}

  .range-row{position:absolute;left:0;width:1200px;display:flex;justify-content:center;gap:80px}
  .range-row--top{top:160px}
  .range-row--bottom{top:1360px}

  .bag-front{position:relative;width:470px;height:880px;background:var(--paper);box-shadow:0 6px 24px rgba(0,0,0,.12)}
  .bag-front--supreme-gold{--accent:var(--gold)}
  .bag-front--organic{--accent:var(--green)}
  .bag-front--eclipse{--accent:var(--navy)}
  .bag-front--supreme-red{--accent:var(--red)}

  .bag-front__seal{position:absolute;top:0;left:0;right:0;height:70px;background:linear-gradient(#f7f7f7,#e6e6e6);border-bottom:1px solid #d8d8d8}

  .carving-mask{position:absolute;top:90px;width:86px;height:96px;background:linear-gradient(160deg,var(--accent),var(--pattern-dark))}
  .carving-band{position:absolute;top:200px;bottom:20px;width:86px;background:repeating-linear-gradient(180deg,var(--accent) 0 60px,var(--pattern-dark) 60px 100px,#f2f2f2 100px 112px)}
  .carving-mask--left,.carving-band--left{left:18px}
  .carving-mask--right,.carving-band--right{right:18px}

  .bag-front__content{position:absolute;left:110px;right:110px;top:170px;text-align:center}
  .brand-name{font-weight:700;color:var(--ink);line-height:1}
  .brand-name__main{display:block;font-size:46px;letter-spacing:-.5px}
  .brand-name__sub{display:block;font-size:20px;letter-spacing:4px;margin-top:16px}

  .blend-label{display:inline-block;margin-top:34px;width:200px;padding:12px 0 8px;background:var(--accent);color:#fff;font-weight:700;font-size:18px;letter-spacing:6px}

  .cup-profile{margin:40px auto 0;width:190px}
  .cup-profile__title{font-weight:700;font-size:12px;letter-spacing:.5px;padding-bottom:10px;border-bottom:1px solid var(--rule)}
  .cup-profile__notes{list-style:none;font-size:13px;line-height:1.55;padding:12px 0 10px;border-bottom:1px solid var(--rule)}

  .brew-methods{display:flex;justify-content:center;gap:16px;margin-top:26px}
  .brew-method{display:flex;flex-direction:column;align-items:center;font-size:9px;gap:4px}
  .brew-method svg{width:24px;height:24px}

  .web-address{margin-top:22px;font-weight:700;font-size:14px;letter-spacing:.5px;color:var(--accent)}
  .net-weight{margin-top:14px;font-weight:700;font-size:26px;color:var(--accent)}

  .identity-panel{position:absolute;left:0;top:2400px;width:1200px;height:600px;background:var(--paper)}
  .identity-mask{position:absolute;top:46px;width:122px;height:198px;background:linear-gradient(160deg,var(--gold) 55%,var(--pattern-dark))}
  .identity-band{position:absolute;top:273px;bottom:0;width:122px;background:linear-gradient(180deg,var(--gold) 0 30%,var(--pattern-dark) 30% 60%,var(--gold) 60% 100%)}
  .identity-mask--left,.identity-band--left{left:239px}
  .identity-mask--right,.identity-band--right{right:239px}
  .identity-panel__name{position:absolute;left:381px;right:381px;top:330px;text-align:center}
  .identity-panel__name .brand-name__main{font-size:80px;letter-spacing:-1px}
  .identity-panel__name .brand-name__sub{font-size:30px;letter-spacing:8px;margin-top:70px}
</style>
</head>
<body>

<section class="range-row range-row--top">
  <article class="bag-front bag-front--supreme-gold">
    <div class="bag-front__seal"></div>
    <div class="carving-mask carving-mask--left" role="img" aria-label="Carved Māori-style mask ornament in gold and black"></div>
    <div class="carving-mask carving-mask--right" role="img" aria-label="Carved Māori-style mask ornament in gold and black"></div>
    <div class="carving-band carving-band--left" role="img" aria-label="Koru scroll pattern band in gold, black and white"></div>
    <div class="carving-band carving-band--right" role="img" aria-label="Koru scroll pattern band in gold, black and white"></div>
    <div class="bag-front__content">
      <h2 class="brand-name"><span class="brand-name__main">Vendra</span><span class="brand-name__sub">coffee co.</span></h2>
      <div class="blend-label">SUPREME</div>
      <div class="cup-profile">
        <h3 class="cup-profile__title">CUP PROFILE:</h3>
        <ul class="cup-profile__notes"><li>Honey</li><li>Stonefruit</li><li>Toffee</li><li>Medium/high sweetness</li></ul>
      </div>
      <div class="brew-methods">
        <div class="brew-method"><svg viewBox="0 0 24 24"><path d="M3 5h18l-7 10h-4z" fill="none" stroke="#2b2b2b" stroke-width="1.5"/></svg>Filter</div>
        <div class="brew-method"><svg viewBox="0 0 24 24"><circle cx="7" cy="8" r="4" fill="none" stroke="#2b2b2b" stroke-width="1.5"/><path d="M10 11l11 9" stroke="#2b2b2b" stroke-width="2.5"/></svg>Espresso</div>
        <div class="brew-method"><svg viewBox="0 0 24 24"><rect x="7" y="6" width="10" height="15" fill="none" stroke="#2b2b2b" stroke-width="1.5"/><path d="M12 2v10M9 2h6" stroke="#2b2b2b" stroke-width="1.5"/></svg>Plunger</div>
        <div class="brew-method"><svg viewBox="0 0 24 24"><ellipse cx="9" cy="8" rx="4" ry="5" fill="#2b2b2b"/><ellipse cx="15" cy="16" rx="4" ry="5" fill="#2b2b2b"/></svg>Beans</div>
      </div>
      <p class="web-address">www.vendracoffee.nz</p>
      <p class="net-weight">1Kg</p>
    </div>
  </article>

  <article class="bag-front bag-front--organic">
    <div class="bag-front__seal"></div>
    <div class="carving-mask carving-mask--left" role="img" aria-label="Carved Māori-style mask ornament in black and green"></div>
    <div class="carving-mask carving-mask--right" role="img" aria-label="Carved Māori-style mask ornament in black and green"></div>
    <div class="carving-band carving-band--left" role="img" aria-label="Zigzag koru pattern band in green, black and white"></div>
    <div class="carving-band carving-band--right" role="img" aria-label="Zigzag koru pattern band in green, black and white"></div>
    <div class="bag-front__content">
      <h2 class="brand-name"><span class="brand-name__main">Vendra</span><span class="brand-name__sub">coffee co.</span></h2>
      <div class="blend-label">ORGANIC</div>
      <div class="cup-profile">
        <h3 class="cup-profile__title">CUP PROFILE:</h3>
        <ul class="cup-profile__notes"><li>Honey</li><li>Stonefruit</li><li>Toffee</li><li>Medium/high sweetness</li></ul>
      </div>
      <div class="brew-methods">
        <div class="brew-method"><svg viewBox="0 0 24 24"><path d="M3 5h18l-7 10h-4z" fill="none" stroke="#2b2b2b" stroke-width="1.5"/></svg>Filter</div>
        <div class="brew-method"><svg viewBox="0 0 24 24"><circle cx="7" cy="8" r="4" fill="none" stroke="#2b2b2b" stroke-width="1.5"/><path d="M10 11l11 9" stroke="#2b2b2b" stroke-width="2.5"/></svg>Espresso</div>
        <div class="brew-method"><svg viewBox="0 0 24 24"><rect x="7" y="6" width="10" height="15" fill="none" stroke="#2b2b2b" stroke-width="1.5"/><path d="M12 2v10M9 2h6" stroke="#2b2b2b" stroke-width="1.5"/></svg>Plunger</div>
        <div class="brew-method"><svg viewBox="0 0 24 24"><ellipse cx="9" cy="8" rx="4" ry="5" fill="#2b2b2b"/><ellipse cx="15" cy="16" rx="4" ry="5" fill="#2b2b2b"/></svg>Beans</div>
      </div>
      <p class="web-address">www.vendracoffee.nz</p>
      <p class="net-weight">1Kg</p>
    </div>
  </article>
</section>

<section class="range-row range-row--bottom">
  <article class="bag-front bag-front--eclipse">
    <div class="bag-front__seal"></div>
    <div class="carving-mask carving-mask--left" role="img" aria-label="Carved Māori-style mask ornament in navy and white"></div>
    <div class="carving-mask carving-mask--right" role="img" aria-label="Carved Māori-style mask ornament in navy and white"></div>
    <div class="carving-band carving-band--left" role="img" aria-label="Fern-spine koru pattern band in navy, black and white"></div>
    <div class="carving-band carving-band--right" role="img" aria-label="Fern-spine koru pattern band in navy, black and white"></div>
    <div class="bag-front__content">
      <h2 class="brand-name"><span class="brand-name__main">Vendra</span><span class="brand-name__sub">coffee co.</span></h2>
      <div class="blend-label">ECLIPSE</div>
      <div class="cup-profile">
        <h3 class="cup-profile__title">CUP PROFILE:</h3>
        <ul class="cup-profile__notes"><li>Honey</li><li>Stonefruit</li><li>Toffee</li><li>Medium/high sweetness</li></ul>
      </div>
      <div class="brew-methods">
        <div class="brew-method"><svg viewBox="0 0 24 24"><path d="M3 5h18l-7 10h-4z" fill="none" stroke="#2b2b2b" stroke-width="1.5"/></svg>Filter</div>
        <div class="brew-method"><svg viewBox="0 0 24 24"><circle cx="7" cy="8" r="4" fill="none" stroke="#2b2b2b" stroke-width="1.5"/><path d="M10 11l11 9" stroke="#2b2b2b" stroke-width="2.5"/></svg>Espresso</div>
        <div class="brew-method"><svg viewBox="0 0 24 24"><rect x="7" y="6" width="10" height="15" fill="none" stroke="#2b2b2b" stroke-width="1.5"/><path d="M12 2v10M9 2h6" stroke="#2b2b2b" stroke-width="1.5"/></svg>Plunger</div>
        <div class="brew-method"><svg viewBox="0 0 24 24"><ellipse cx="9" cy="8" rx="4" ry="5" fill="#2b2b2b"/><ellipse cx="15" cy="16" rx="4" ry="5" fill="#2b2b2b"/></svg>Beans</div>
      </div>
      <p class="web-address">www.vendracoffee.nz</p>
      <p class="net-weight">1Kg</p>
    </div>
  </article>

  <article class="bag-front bag-front--supreme-red">
    <div class="bag-front__seal"></div>
    <div class="carving-mask carving-mask--left" role="img" aria-label="Carved Māori-style mask ornament in black and red"></div>
    <div class="carving-mask carving-mask--right" role="img" aria-label="Carved Māori-style mask ornament in black and red"></div>
    <div class="carving-band carving-band--left" role="img" aria-label="Spiral koru pattern band in red, black and white"></div>
    <div class="carving-band carving-band--right" role="img" aria-label="Spiral koru pattern band in red, black and white"></div>
    <div class="bag-front__content">
      <h2 class="brand-name"><span class="brand-name__main">Vendra</span><span class="brand-name__sub">coffee co.</span></h2>
      <div class="blend-label">SUPREME</div>
      <div class="cup-profile">
        <h3 class="cup-profile__title">CUP PROFILE:</h3>
        <ul class="cup-profile__notes"><li>Honey</li><li>Stonefruit</li><li>Toffee</li><li>Medium/high sweetness</li></ul>
      </div>
      <div class="brew-methods">
        <div class="brew-method"><svg viewBox="0 0 24 24"><path d="M3 5h18l-7 10h-4z" fill="none" stroke="#2b2b2b" stroke-width="1.5"/></svg>Filter</div>
        <div class="brew-method"><svg viewBox="0 0 24 24"><circle cx="7" cy="8" r="4" fill="none" stroke="#2b2b2b" stroke-width="1.5"/><path d="M10 11l11 9" stroke="#2b2b2b" stroke-width="2.5"/></svg>Espresso</div>
        <div class="brew-method"><svg viewBox="0 0 24 24"><rect x="7" y="6" width="10" height="15" fill="none" stroke="#2b2b2b" stroke-width="1.5"/><path d="M12 2v10M9 2h6" stroke="#2b2b2b" stroke-width="1.5"/></svg>Plunger</div>
        <div class="brew-method"><svg viewBox="0 0 24 24"><ellipse cx="9" cy="8" rx="4" ry="5" fill="#2b2b2b"/><ellipse cx="15" cy="16" rx="4" ry="5" fill="#2b2b2b"/></svg>Beans</div>
      </div>
      <p class="web-address">www.vendracoffee.nz</p>
      <p class="net-weight">1Kg</p>
    </div>
  </article>
</section>

<section class="identity-panel">
  <div class="identity-mask identity-mask--left" role="img" aria-label="Large carved Māori-style mask ornament in gold and black"></div>
  <div class="identity-mask identity-mask--right" role="img" aria-label="Large carved Māori-style mask ornament in gold and black"></div>
  <div class="identity-band identity-band--left" role="img" aria-label="Koru scroll ornament in gold and black"></div>
  <div class="identity-band identity-band--right" role="img" aria-label="Koru scroll ornament in gold and black"></div>
  <h1 class="brand-name identity-panel__name"><span class="brand-name__main">Vendra</span><span class="brand-name__sub">coffee co.</span></h1>
</section>

</body>
</html>
```